New Managed IT company needs a business card

We are an IT management and support company that needs a business card design. I have a logo that I'll provide. Blues and blacks match the logo, but i'm open to anything. I want the card to help people take us seriously, but still have some energy and fun in it. The card should communicate stability and a solid company.

Target Market(s)

Target market includes Owners and Presidents at small businesses of 20 - 100 employees in the Pittsburgh PA area.

Industry/Entity Type

Information Technology

Contact Information for Business Card

i am open to other designs, but i imagine having only the logo on one side and then the logo plus all contact details on the other side.

Requirements
Must have
• Our logo
• Company name is optional if the logo makes it obvious
• A name - Lew Tasker
• A title - President
• A phone number - 724-XXX-XXXX
• A mobile phone number - 724-516-0471
• An email address - ltasker@brightlanetech.com
• a website - brightlanetech.com or www.brightlanetech.com
Nice to have
• some people tell me the logo feels like a superhero theme, some fun with that idea might be good. I'm open to ideas.
Should not have
• stock photos of people or computers - especially old looking stuff.

```html
<!DOCTYPE html>
<html lang="en">
<head>
<meta charset="utf-8">
<title>Brightlane Tech — Business Card</title>
<link href="https://fonts.googleapis.com/css2?family=Lato:wght@400&family=Roboto:wght@400;500&display=swap" rel="stylesheet">
<style>
  :root {
    --page-bg: #d9dde2;
    --brand-blue: #0277c4;
    --card-light: #eef1f4;
    --ink: #1c1c1e;
    --white: #ffffff;
    --faint-mark: #e3e6ea;
  }
  * { margin: 0; padding: 0; box-sizing: border-box; }
  html, body { width: 1200px; height: 848px; overflow: hidden; }
  body { background: var(--page-bg); position: relative; font-family: "Roboto", sans-serif; }

  .card {
    position: absolute;
    left: 272px;
    width: 632px;
    height: 356px;
    border-radius: 19px;
    overflow: hidden;
    box-shadow: 0 6px 16px rgba(0,0,0,0.18);
  }

  /* Front */
  .card--front { top: 38px; background: var(--brand-blue); color: var(--white); }
  .front-mark {
    position: absolute; left: 271px; top: 104px;
    width: 90px; height: 90px; border-radius: 50%;
    background: var(--ink); border: 6px solid var(--white);
  }
  .front-name {
    position: absolute; left: 0; right: 0; top: 224px;
    text-align: center; font-family: "Roboto", sans-serif; font-weight: 500;
    font-size: 34px; letter-spacing: 4px; text-transform: uppercase;
  }
  .front-url {
    position: absolute; left: 0; right: 0; top: 306px;
    text-align: center; font-family: "Lato", sans-serif; font-size: 14.5px;
  }

  /* Back */
  .card--back { top: 438px; background: var(--card-light); color: var(--ink); }
  .back-watermark {
    position: absolute; left: 330px; top: 106px;
    width: 304px; height: 304px; border-radius: 50%;
    background: var(--faint-mark);
  }
  .back-mark {
    position: absolute; left: 113px; top: 24px;
    width: 80px; height: 80px; border-radius: 50%;
    background: var(--ink); border: 6px solid var(--brand-blue);
  }
  .back-company {
    position: absolute; left: 40px; top: 120px;
    font-weight: 500; font-size: 26px; letter-spacing: 3px;
    text-transform: uppercase; color: var(--ink);
  }
  .person-name {
    position: absolute; left: 40px; top: 185px;
    font-size: 22.5px; font-weight: 400; color: var(--brand-blue);
  }
  .person-title {
    position: absolute; left: 40px; top: 216px; font-size: 14.5px;
  }
  .contact-list {
    position: absolute; left: 40px; top: 255px; list-style: none;
    font-family: "Lato", sans-serif; font-size: 15px; line-height: 20px;
  }
  .contact-list li { display: flex; align-items: center; gap: 4px; }
  .contact-list svg { width: 13px; height: 13px; flex: none; }
  .link-domain { color: var(--brand-blue); }
</style>
</head>
<body>
  <section class="card card--front">
    <div class="front-mark"></div>
    <div class="front-name">Brightlane Tech</div>
    <div class="front-url">www.brightlanetech.com</div>
  </section>

  <section class="card card--back">
    <div class="back-watermark"></div>
    <div class="back-mark"></div>
    <div class="back-company">Brightlane Tech</div>
    <div class="person-name">Lew Tasker</div>
    <div class="person-title">President</div>
    <ul class="contact-list">
      <li>
        <svg viewBox="0 0 16 16"><path fill="#0277c4" d="M3.5 1l3 3-1.6 2a9 9 0 0 0 5 5l2-1.6 3 3-2 2.3C7 14 2 9 1.2 3z"/></svg>
        724-XXX-XXXX
      </li>
      <li>
        <svg viewBox="0 0 16 16"><rect x="4" y="1" width="8" height="14" rx="1.5" fill="none" stroke="#0277c4" stroke-width="1.6"/><rect x="6.5" y="12" width="3" height="1.2" fill="#0277c4"/></svg>
        724-516-0471
      </li>
      <li>
        <svg viewBox="0 0 16 16"><rect x="1" y="3.5" width="14" height="9" fill="#0277c4"/><path d="M1 3.5l7 5 7-5" fill="none" stroke="#eef1f4" stroke-width="1.2"/></svg>
        ltasker@brightlanetech.com
      </li>
      <li>
        <svg viewBox="0 0 16 16"><circle cx="8" cy="8" r="6.5" fill="none" stroke="#0277c4" stroke-width="1.5"/><ellipse cx="8" cy="8" rx="3" ry="6.5" fill="none" stroke="#0277c4" stroke-width="1.2"/><path d="M1.5 8h13" stroke="#0277c4" stroke-width="1.2"/></svg>
        <span>www.<span class="link-domain">brightlanetech</span>.com</span>
      </li>
    </ul>
  </section>
</body>
</html>
```